Medical clinic VALORENT sales materials presentation folder

I am looking for a professional design to a sales/presentation folder for VALORENT medical clinic. I would like to get picture of doctor in a class design.
I had an example of a hold marketing and the VALORENT LOGO.
VALORENT have 5 clinics and we are serious whit lot of doctors. We are doing lot of medical service. I put a doctor picture, but if you have a better choice for the presentation folder don't hesitate to use it.

Target Market(s)

Medical customer and corporation

Industry/Entity Type

Health care

Requirements
Must have
• Professional design - red accent
Nice to have
• Medical doctor picture
Should not have
• Don't want the same hold design that the example

```html
<!DOCTYPE html>
<html lang="en">
<head>
<meta charset="utf-8">
<title>VALORENT presentation folder</title>
<link rel="stylesheet" href="https://fonts.googleapis.com/css2?family=Poppins:wght@400;600;700;800&family=Montserrat:wght@500;600&display=swap">
<style>
  :root {
    --red: #e4202a;
    --red-deep: #d81920;
    --red-soft: #f7b7ae;
    --ink: #111111;
    --paper: #ffffff;
    --paper-grey: #f1f1f2;
    --stage: #e3e3e4;
    --flap: #f4f4f5;
  }
  * { margin: 0; padding: 0; box-sizing: border-box; }
  html, body { width: 1200px; height: 935px; overflow: hidden; }
  body {
    position: relative;
    background: var(--stage);
    font-family: "Poppins", sans-serif;
    color: var(--ink);
  }
  .dieline { position: absolute; left: 0; top: 0; }
  .panel {
    position: absolute;
    top: 131px;
    width: 466px;
    height: 601px;
    overflow: hidden;
    background: linear-gradient(180deg, var(--paper-grey) 0%, var(--paper) 42%, #fde7e3 62%, var(--red-soft) 80%, #ef5a52 93%, var(--red-deep) 100%);
  }
  .panel--back { left: 178px; }
  .panel--front { left: 642px; border-left: 1px solid #e6e6e6; }

  .web-band {
    position: absolute;
    left: 0; right: 0;
    top: 563px;
    height: 2px;
    background: var(--paper);
  }
  .web-pill {
    position: absolute;
    top: 555px;
    left: 50%;
    transform: translateX(-50%);
    background: var(--paper);
    padding: 1px 6px;
    font-family: "Montserrat", sans-serif;
    font-weight: 600;
    font-size: 11.5px;
    letter-spacing: 2.6px;
    color: var(--ink);
    white-space: nowrap;
  }
  .web-pill .accent { color: var(--red); }

  .back-name {
    position: absolute;
    top: 272px;
    left: 0; right: 0;
    text-align: center;
    font-weight: 800;
    font-size: 41px;
    letter-spacing: 1px;
    line-height: 1;
  }
  .contact {
    position: absolute;
    top: 330px;
    left: 0; right: 0;
    text-align: center;
  }
  .contact__kicker { color: var(--red); font-weight: 600; font-size: 11px; line-height: 1.2; }
  .contact__title { font-weight: 800; font-size: 26px; line-height: 1.1; }
  .contact__rule { width: 33px; height: 2px; background: var(--red); margin: 6px auto 6px; }
  .contact__item { font-size: 8.6px; line-height: 1.3; margin-bottom: 7px; }
  .contact__icon { display: block; margin: 0 auto 2px; }

  .front-brand {
    position: absolute;
    top: 54px;
    left: 97px;
    display: flex;
    align-items: center;
    gap: 12px;
  }
  .front-brand__mark { width: 24px; height: 24px; background: var(--red); }
  .front-brand__name { font-weight: 800; font-size: 30px; letter-spacing: 1px; line-height: 1; }

  .doctor-photo {
    position: absolute;
    left: 7px;
    top: 132px;
    width: 380px;
    height: 420px;
    border-radius: 40% 40% 8px 8px;
    background: radial-gradient(ellipse at 50% 35%, #e9dcd3 0%, #d8c6bb 35%, rgba(240,210,205,0.5) 70%, rgba(255,255,255,0) 100%);
  }
</style>
</head>
<body>
  <svg class="dieline" width="1200" height="935" aria-hidden="true">
    <polygon points="93,185 178,131 178,732 93,680" fill="var(--flap)"/>
    <polygon points="178,732 642,732 598,826 224,826" fill="var(--flap)"/>
  </svg>

  <section class="panel panel--back">
    <h2 class="back-name">VALORENT</h2>
    <div class="contact">
      <p class="contact__kicker">Get in touch</p>
      <h3 class="contact__title">Contact</h3>
      <div class="contact__rule"></div>
      <div class="contact__item">
        <svg class="contact__icon" width="11" height="11" viewBox="0 0 12 12"><circle cx="6" cy="6" r="6" fill="var(--red)"/><path d="M4 3.2l1 1.4-.6.7c.4.9 1 1.5 1.9 1.9l.7-.6 1.4 1-.5 1c-2.4-.3-4.2-2.1-4.5-4.5z" fill="#fff"/></svg>
        418 555-0147
      </div>
      <div class="contact__item">
        <svg class="contact__icon" width="11" height="11" viewBox="0 0 12 12"><circle cx="6" cy="6" r="6" fill="var(--red)"/><rect x="3" y="4" width="6" height="4.2" rx="0.6" fill="#fff"/><path d="M3 4.2l3 2.2 3-2.2" stroke="var(--red)" stroke-width="0.7" fill="none"/></svg>
        info@valorentmed.com
      </div>
      <div class="contact__item">
        <svg class="contact__icon" width="11" height="11" viewBox="0 0 12 12"><circle cx="6" cy="6" r="6" fill="var(--red)"/><path d="M6 2.8a2.2 2.2 0 0 1 2.2 2.2c0 1.6-2.2 3.9-2.2 3.9S3.8 6.6 3.8 5A2.2 2.2 0 0 1 6 2.8z" fill="#fff"/><circle cx="6" cy="5" r="0.8" fill="var(--red)"/></svg>
        415, rue des Érables, local 120 Québec<br>(Québec) G1A 0B4
      </div>
    </div>
    <div class="web-band"></div>
    <p class="web-pill">www.<span class="accent">valorent</span>.ca</p>
  </section>

  <section class="panel panel--front">
    <div class="front-brand">
      <span class="front-brand__mark"></span>
      <h1 class="front-brand__name">VALORENT</h1>
    </div>
    <div class="doctor-photo" role="img" aria-label="Photo of a smiling doctor in a white coat with a stethoscope, writing on a clipboard"></div>
    <div class="web-band"></div>
    <p class="web-pill">www.<span class="accent">valorent</span>.ca</p>
  </section>
</body>
</html>
```